Email Marketing Newsletter Design

Require the design of a email marketing newsletter. I will convert it into an updatable html template. I have supplied the copy for the first edition.

The newsletter is for a company that provides commercial property maintenance services such as office cleaning, lawns & gardens, electrical work etc

Web Site for client is:

http://brenvoli.com.au/cgi-bin/xmlweb.cgi/home/index_html
Updates

Hi Maud

I will upload the doc as a PDF.

The width needs to be 777px

Look forward to seeing your design

Rgds
Derek

Target Market(s)

Property Facility Managers and Maintenance Managers working for commerical office buildings and large corporate sites

Industry/Entity Type

Construction

Number of Pages Required

1 page

Requirements
Must have
• Must be 777px wide
• Strong branding

• Intro paragraph

• Monthly Specials section

• Service Feature section

• Simple but clean with strong design elements
Nice to have
• Send to a friend icon

```html
<!DOCTYPE html>
<html lang="en">
<head>
<meta charset="utf-8">
<title>Brenvoli Property Services Group – December 2009 Newsletter</title>
<link rel="stylesheet" href="https://fonts.googleapis.com/css2?family=Source+Sans+3:ital,wght@0,400;0,600;0,700;1,400;1,600&family=Arimo:ital,wght@0,400;0,700;1,400&display=swap">
<style>
  :root {
    --navy: #003a80;
    --blue: #0f4f9c;
    --blue-light: #2f6fc0;
    --green: #5a9a2c;
    --green-light: #8cc63f;
    --rule: #b7d88f;
    --text: #555555;
    --muted: #9a9a9a;
    --white: #ffffff;
    --orange: #f0a050;
    --orange-dark: #e07d22;
  }
  * { box-sizing: border-box; margin: 0; padding: 0; }
  html, body { width: 717px; height: 1200px; overflow: hidden; background: var(--white); }
  .newsletter {
    position: relative; width: 777px; height: 1290px;
    transform: scale(0.923); transform-origin: 0 0;
    font-family: "Arimo", Arial, sans-serif; color: var(--text);
  }
  .abs { position: absolute; }

  /* Masthead */
  .masthead { left: 0; top: 0; width: 777px; height: 190px; }
  .masthead-phone { right: 16px; top: 10px; color: var(--white); font: 400 22px "Source Sans 3", sans-serif; }
  .brand { left: 30px; top: 30px; display: flex; align-items: center; gap: 14px; }
  .brand-mark { width: 60px; height: 52px; background: var(--white); }
  .brand-name { color: var(--white); font: 700 62px/1 "Source Sans 3", sans-serif; letter-spacing: 2px; }
  .brand-tagline { left: 172px; top: 88px; color: var(--white); font: 400 23px "Source Sans 3", sans-serif; }
  .issue-date { left: 504px; top: 143px; color: var(--white); font: italic 400 17px "Source Sans 3", sans-serif; }
  .edition-badge { left: 666px; top: 55px; width: 108px; height: 108px; }

  /* Navigation */
  .main-nav {
    left: 8px; top: 205px; width: 510px; height: 31px; border-radius: 4px;
    background: linear-gradient(var(--blue-light), var(--navy));
    display: flex; align-items: center;
  }
  .main-nav a {
    color: var(--white); text-decoration: none; font: 400 14px "Source Sans 3", sans-serif;
    padding: 0 14px; border-left: 1px solid rgba(255,255,255,.25);
  }
  .main-nav a:first-child { border-left: 0; padding-left: 20px; }

  /* Sections */
  .section-title { color: var(--navy); font: 600 24px/1.2 "Source Sans 3", sans-serif; }
  .section-rule { height: 2px; background: linear-gradient(90deg, var(--rule), var(--green-light) 50%, rgba(183,216,143,0)); }
  .photo {
    width: 142px; height: 142px; border: 2px solid var(--white);
    box-shadow: 1px 2px 4px rgba(0,0,0,.35);
    background: linear-gradient(180deg, #3f86d6 0%, #8cb9e8 45%, #1d4f8c 100%);
  }
  .copy { font-size: 13px; line-height: 17px; }
  .copy p + p { margin-top: 17px; }
  .copy em { font-style: italic; }
  .highlight { color: var(--green); font-weight: 700; }
  .section-badge { width: 80px; height: 80px; }

  /* Sidebar */
  .side-panel {
    left: 537px; width: 230px; border-radius: 6px; overflow: hidden;
    background: linear-gradient(var(--blue-light), var(--navy));
    color: var(--white);
  }
  .side-panel h2 { font: 400 18px "Source Sans 3", sans-serif; padding: 13px 12px 8px; }
  .side-panel .swoosh { position: absolute; left: 0; bottom: 0; width: 230px; height: 40px; }
  .side-list { list-style: none; padding: 0 12px; }
  .side-list li {
    position: relative; padding-left: 37px; font: 400 13.5px/17px "Source Sans 3", sans-serif; margin-bottom: 2px;
  }
  .side-list li::before {
    content: ""; position: absolute; left: 2px; top: 6px; width: 24px; height: 4px; background: var(--white);
  }
  .side-list strong { font-weight: 700; display: block; }
  .forward-text { padding: 0 13px; font: 400 13.5px/17px "Source Sans 3", sans-serif; }
  .forward-button {
    display: block; margin: 16px auto 0; width: 194px; height: 33px; border-radius: 5px;
    background: linear-gradient(var(--orange), var(--orange-dark));
    border: 1px solid #c86a18; color: var(--navy); text-align: center;
    font: 700 17px/31px "Source Sans 3", sans-serif; text-decoration: none;
  }

  .unsubscribe { left: 0; top: 1270px; width: 777px; text-align: center; font-size: 11px; color: var(--muted); }
  .unsubscribe a { color: var(--green); text-decoration: none; }
</style>
</head>
<body>
<svg width="0" height="0" style="position:absolute">
  <defs>
    <symbol id="starburst" viewBox="0 0 80 80">
      <polygon points="78,40 69.9,48 72.9,59 61.9,61.9 59,72.9 48,69.9 40,78 32,69.9 21,72.9 18.1,61.9 7.1,59 10.1,48 2,40 10.1,32 7.1,21 18.1,18.1 21,7.1 32,10.1 40,2 48,10.1 59,7.1 61.9,18.1 72.9,21 69.9,32"/>
    </symbol>
  </defs>
</svg>

<div class="newsletter">
  <header class="masthead abs">
    <svg class="abs" style="left:0;top:0" width="777" height="190" viewBox="0 0 777 190">
      <defs>
        <linearGradient id="swooshGreen" x1="0" x2="1">
          <stop offset="0" stop-color="#2e6e1e"/><stop offset="1" stop-color="#8cc63f"/>
        </linearGradient>
      </defs>
      <path d="M4 4 H773 V150 C640 175 520 190 380 178 C230 165 110 135 4 125 Z" fill="#003a80"/>
      <path d="M360 176 C520 190 650 170 773 112 V132 C660 180 520 195 360 176 Z" fill="url(#swooshGreen)"/>
    </svg>
    <div class="masthead-phone abs">Call 1300 55 01 82</div>
    <div class="brand abs">
      <span class="brand-mark"></span>
      <span class="brand-name">BRENVOLI</span>
    </div>
    <div class="brand-tagline abs">Property Services Group</div>
    <div class="issue-date abs">December, 2009</div>
    <svg class="edition-badge abs" viewBox="0 0 80 80">
      <use href="#starburst" fill="#7cc23a"/>
      <g transform="rotate(-22 40 40)" fill="#0f3f86" font-family="Source Sans 3, sans-serif" font-weight="700" font-style="italic" text-anchor="middle">
        <text x="40" y="37" font-size="12">1st</text>
        <text x="40" y="50" font-size="12">EDITION</text>
      </g>
    </svg>
  </header>

  <nav class="main-nav abs">
    <a href="#">About us</a><a href="#">Divisions</a><a href="#">Articles &amp; Podcasts</a><a href="#">Locations</a><a href="#">Industry News</a>
  </nav>

  <!-- Welcome -->
  <h1 class="section-title abs" style="left:19px;top:262px">Welcome</h1>
  <div class="section-rule abs" style="left:10px;top:292px;width:510px"></div>
  <div class="photo abs" style="left:17px;top:316px" role="img" aria-label="Photo of a modern curved glass office tower"></div>
  <div class="copy abs" style="left:180px;top:316px;width:330px">
    <p><em>Brenvoli</em> is pleased to present our <span class="highlight">first e-newsletter</span>. We believe in making life easier for our clients. So, we have created an e-newsletter to let you know about our current promotions and the services that we offer.</p>
    <p>Please enjoy learning about the range of ways <em>Brenvoli</em> can look after your office cleaning and maintenance needs.</p>
  </div>

  <!-- Monthly special -->
  <svg class="section-badge abs" style="left:8px;top:500px" viewBox="0 0 80 80">
    <use href="#starburst" fill="#5aa530"/>
    <g transform="rotate(-25 40 40)" fill="#fff" font-family="Source Sans 3, sans-serif" font-weight="600" font-style="italic" text-anchor="middle">
      <text x="40" y="38" font-size="13">Special</text>
      <text x="40" y="52" font-size="13">Offer</text>
    </g>
  </svg>
  <h2 class="section-title abs" style="left:93px;top:524px;width:420px">December Offer: FREE Expert Brenvoli Carpet and Window Clean</h2>
  <div class="section-rule abs" style="left:10px;top:587px;width:510px"></div>
  <div class="photo abs" style="left:17px;top:607px" role="img" aria-label="Photo of a modern curved glass office tower"></div>
  <div class="copy abs" style="left:180px;top:606px;width:320px">
    <p>At <em>Brenvoli</em>, we believe in rewarding our loyal customers. This month, we are offering a <span class="highlight">FREE</span> carpet and window clean if you engage our standard office cleaning services for at least 6 months.<br><span class="highlight">There are no strings attached and no contracts to sign!</span></p>
    <p>Call <em>Brenvoli</em> today and allow us to manage all of your cleaning needs for you!</p>
  </div>

  <!-- Service spotlight -->
  <svg class="section-badge abs" style="left:8px;top:797px" viewBox="0 0 80 80">
    <use href="#starburst" fill="#1d5fb0"/>
    <g transform="rotate(-25 40 40)" fill="#fff" font-family="Source Sans 3, sans-serif" font-weight="600" font-style="italic" text-anchor="middle">
      <text x="40" y="45" font-size="13">Spotlight</text>
    </g>
  </svg>
  <h2 class="section-title abs" style="left:93px;top:847px">Brenvoli Cleaning Services</h2>
  <div class="section-rule abs" style="left:10px;top:881px;width:510px"></div>
  <div class="photo abs" style="left:17px;top:898px" role="img" aria-label="Photo of a modern curved glass office tower"></div>
  <div class="copy abs" style="left:180px;top:894px;width:320px">
    <p>A <em>Brenvoli</em> office clean will look after all aspects of your office site. Our service includes regularly and thoroughly cleaning: floors, desks, kitchens and bathrooms. We also look after: window cleaning, carpet cleaning, vinyl floor stripping sealing, Venetian blind cleaning, floor sweeping, floor scrubbing, high pressure cleaning, ceiling tile and light cleaning and graffiti removal.</p>
  </div>
  <div class="copy abs" style="left:21px;top:1060px;width:470px">
    <p>We realise that cleaning should be a background activity. You won’t notice we are there; you will notice that you don’t need to self manage the cleaning process, we do that for you.</p>
    <p>Allow our experienced, expert staff to project manage all of your regular, and irregular, office cleaning needs!</p>
  </div>

  <!-- Sidebar -->
  <aside class="side-panel abs" style="top:296px;height:174px">
    <h2>In this issue</h2>
    <ul class="side-list">
      <li>Welcome</li>
      <li>December Offer: FREE Expert Brenvoli Carpet and Window Clean</li>
      <li>Spotlight: Brenvoli Cleaning Services</li>
    </ul>
    <svg class="swoosh" viewBox="0 0 230 40" preserveAspectRatio="none"><path d="M0 26 C80 44 170 30 230 0 V40 H0 Z" fill="#5aa530"/></svg>
  </aside>

  <aside class="side-panel abs" style="top:486px;height:173px">
    <h2>Forward this email</h2>
    <p class="forward-text">Do you know someone who might be interested in receiving this newsletter?</p>
    <a class="forward-button" href="#">Forward to a Friend</a>
    <svg class="swoosh" viewBox="0 0 230 40" preserveAspectRatio="none"><path d="M0 26 C80 44 170 30 230 0 V40 H0 Z" fill="#5aa530"/></svg>
  </aside>

  <aside class="side-panel abs" style="top:676px;height:237px">
    <h2>Contact us</h2>
    <ul class="side-list">
      <li><strong>Phone:</strong>1300 55 01 82</li>
      <li><strong>Fax:</strong>02 9555 0173</li>
      <li><strong>Postal Address:</strong>PO Box 412, Marlowe NSW 1899</li>
      <li><strong>Head Office:</strong>Unit 7, 41 Ashby Street, Marlowe NSW 2199</li>
    </ul>
    <svg class="swoosh" viewBox="0 0 230 40" preserveAspectRatio="none"><path d="M0 26 C80 44 170 30 230 0 V40 H0 Z" fill="#5aa530"/></svg>
  </aside>

  <p class="unsubscribe abs">If you don't want to receive these emails any more, please unsubscribe <a href="#">here</a></p>
</div>
</body>
</html>
```